Brevant Business Card

I have a business that is called "Brevant Electrical Products LTD" My company deals with top of the range laptops and mobile phones that are exclusive. I need a business card that will be eye catching but not over complicated.

Target Market(s)

Adults aged 19 to 50
Upper middle class

Industry/Entity Type

Business

Requirements
Must have
• Company name/logo (file attached)
• It must have my contact information which is:

• Name: Dale Marwick

• Position: Managing Director 

• Business Address: 7 Hapton Row, London, W4 9QD

• Contact Number: 02085193604
• Mobile: 07814260537
• Email: info@brevant-goods.co.uk
Nice to have
• Simple and stylish
• Eye catching

```html
<!DOCTYPE html>
<html lang="en">
<head>
<meta charset="utf-8">
<title>Brevant Electrical Products – Business Card Options</title>
<link rel="stylesheet" href="https://fonts.googleapis.com/css2?family=Arimo&family=Belleza&family=EB+Garamond&family=Questrial&display=swap">
<style>
  :root {
    --page: #ffffff;
    --frame: #c9c9c9;
    --ink: #1c1c1c;
    --card-border: #3a3a3a;
    --brand-blue: #0a84cf;
    --rule-blue: #1b9ad9;
    --band-blue: #4db4e9;
    --pale: #f7fbff;
  }
  * { margin: 0; padding: 0; box-sizing: border-box; }
  html, body { width: 876px; height: 1200px; overflow: hidden; background: var(--page); }
  .sheet {
    position: relative; width: 876px; height: 1200px;
    border: 1px solid var(--frame); background: var(--page); color: var(--ink);
  }
  .sheet-heading {
    position: absolute; left: 0; width: 876px; text-align: center;
    font-family: "Arimo", Arial, sans-serif; font-size: 34px; top: 34px; line-height: 1;
  }
  .section-heading {
    position: absolute; left: 0; width: 840px; text-align: center;
    font-family: "EB Garamond", Georgia, serif; font-size: 32px; top: 598px; line-height: 1;
  }
  .card {
    position: absolute; width: 379px; height: 232px;
    border: 1px solid var(--card-border); background: var(--page);
    box-shadow: 4px 5px 5px rgba(0,0,0,0.35); overflow: hidden;
  }
  .col-left { left: 41px; }
  .col-right { left: 451px; }
  .row-1 { top: 79px; } .row-2 { top: 347px; } .row-3 { top: 650px; } .row-4 { top: 917px; }

  .fade-bottom { background: linear-gradient(to bottom, var(--pale) 0%, var(--pale) 72%, #cfe9f9 82%, var(--band-blue) 100%); }
  .fade-bottom-long { background: linear-gradient(to bottom, var(--pale) 0%, var(--pale) 42%, #d8eefb 70%, var(--band-blue) 100%); }
  .band-left { background: linear-gradient(to right, var(--band-blue) 0%, var(--band-blue) 36%, #dff1fc 68%, var(--pale) 78%, var(--page) 100%); }
  .band-right { background: linear-gradient(to right, var(--page) 0%, var(--pale) 48%, #c5e6f9 70%, var(--band-blue) 86%, var(--band-blue) 100%); }

  .t { position: absolute; white-space: nowrap; line-height: 1; }
  .brand { font-family: "Questrial", Arial, sans-serif; color: var(--brand-blue); font-size: 58px; letter-spacing: 2px; }
  .brand-small { font-size: 40px; letter-spacing: 1px; }
  .brand-vertical { color: #ffffff; font-size: 44px; letter-spacing: 1px; transform: translate(-50%, -50%) rotate(-90deg); }
  .tagline { font-family: "Questrial", Arial, sans-serif; font-size: 26px; letter-spacing: 3.4px; color: var(--ink); }
  .tagline-small { font-size: 19px; letter-spacing: 2.2px; }
  .tagline-vertical { font-size: 19px; letter-spacing: 2.6px; transform: translate(-50%, -50%) rotate(-90deg); }
  .person-name { font-family: "Belleza", "Optima", sans-serif; font-size: 21px; }
  .person-role { font-family: "Belleza", "Optima", sans-serif; font-size: 15px; }
  .contact { font-family: "Belleza", "Optima", sans-serif; font-size: 12.5px; line-height: 15.6px; }
  .contact-large { font-size: 14px; line-height: 17.2px; }
  .sans .person-name, .sans .person-role, .sans.contact { font-family: "Questrial", Arial, sans-serif; }
  .right-align { text-align: right; }
  .rule-v { position: absolute; width: 1.5px; background: var(--rule-blue); }
  .rule-h { position: absolute; height: 1.5px; background: var(--rule-blue); }
</style>
</head>
<body>
<main class="sheet">
  <h1 class="sheet-heading" style="font-weight:400">STAMPING: Two sides</h1>

  <!-- Option 1: front -->
  <section class="card col-left row-1 fade-bottom">
    <div class="t brand" style="left:50px; top:125px;">BREVANT</div>
    <div class="t tagline" style="left:50px; top:196px;">Electrical Products</div>
  </section>
  <!-- Option 1: back -->
  <section class="card col-right row-1">
    <div class="t person-name" style="left:17px; top:23px;">Dale Marwick</div>
    <div class="t person-role" style="left:17px; top:47px;">Managing Director</div>
    <div class="rule-v" style="left:153px; top:24px; height:186px;"></div>
    <div class="t contact" style="left:164px; top:22px;">Phone: 02085193604<br>Mobile: 07814260537<br>Email: info@brevant-goods.co.uk</div>
    <div class="t contact" style="left:164px; top:196px;">7 Hapton Row, London, W4 9QD UK</div>
  </section>

  <!-- Option 2: front -->
  <section class="card col-left row-2 fade-bottom">
    <div class="t brand" style="left:50px; top:125px;">BREVANT</div>
    <div class="t tagline" style="left:50px; top:196px;">Electrical Products</div>
  </section>
  <!-- Option 2: back -->
  <section class="card col-right row-2">
    <div class="t person-name right-align" style="right:21px; top:21px;">Dale Marwick</div>
    <div class="t person-role right-align" style="right:21px; top:45px;">Managing Director</div>
    <div class="rule-h" style="left:20px; top:72px; width:337px;"></div>
    <div class="t contact contact-large" style="left:20px; top:136px;">Phone: 02085193604<br>Mobile: 07814260537<br>Email: info@brevant-goods.co.uk<br>7 Hapton Row, London, W4 9QD UK</div>
  </section>

  <h2 class="section-heading" style="font-weight:400">Single side</h2>

  <!-- Option 3 -->
  <section class="card col-left row-3 band-left">
    <div class="t brand brand-vertical" style="left:50px; top:116px;">BREVANT</div>
    <div class="t person-name right-align" style="right:17px; top:19px;">Dale Marwick</div>
    <div class="t person-role right-align" style="right:17px; top:44px;">Managing Director</div>
    <div class="t contact contact-large right-align" style="right:17px; top:121px; line-height:16.6px;">Phone: 02085193604<br>Mobile: 07814260537<br>Email: info@brevant-goods.co.uk<br>7 Hapton Row, London, W4 9QD UK</div>
    <div class="t tagline tagline-small" style="right:17px; top:199px; font-size:23px; letter-spacing:3px;">Electrical Products</div>
  </section>

  <!-- Option 4 -->
  <section class="card col-right row-3 fade-bottom-long">
    <div class="t person-name" style="left:17px; top:22px;">Dale Marwick</div>
    <div class="t person-role" style="left:17px; top:46px;">Managing Director</div>
    <div class="rule-v" style="left:153px; top:24px; height:58px;"></div>
    <div class="t contact" style="left:164px; top:23px;">Phone: 02085193604<br>Mobile: 07814260537<br>Email: info@brevant-goods.co.uk<br>7 Hapton Row, London, W4 9QD UK</div>
    <div class="t brand" style="left:45px; top:125px;">BREVANT</div>
    <div class="t tagline" style="left:45px; top:196px;">Electrical Products</div>
  </section>

  <!-- Option 5 -->
  <section class="card col-left row-4 band-right">
    <div class="t person-name" style="left:16px; top:15px;">Dale Marwick</div>
    <div class="t person-role" style="left:16px; top:38px;">Managing Director</div>
    <div class="t contact" style="left:15px; top:156px;">Phone: 02085193604<br>Mobile: 07814260537<br>Email: info@brevant-goods.co.uk<br>7 Hapton Row, London, W4 9QD UK</div>
    <div class="t brand brand-vertical" style="left:314px; top:116px;">BREVANT</div>
    <div class="t tagline tagline-vertical" style="left:350px; top:116px;">Electrical Products</div>
  </section>

  <!-- Option 6 -->
  <section class="card col-right row-4 sans">
    <div class="t brand brand-small" style="left:19px; top:22px;">BREVANT</div>
    <div class="t tagline tagline-small" style="left:19px; top:70px;">Electrical Products</div>
    <div class="rule-h" style="left:20px; top:92px; width:337px;"></div>
    <div class="t person-name right-align" style="right:22px; top:102px; font-family:'Questrial', Arial, sans-serif;">Dale Marwick</div>
    <div class="t person-role right-align" style="right:22px; top:126px; font-family:'Questrial', Arial, sans-serif;">Managing Director</div>
    <div class="t contact sans" style="left:20px; top:158px;">Phone: 02085193604<br>Mobile: 07814260537<br>Email: info@brevant-goods.co.uk<br>7 Hapton Row, London, W4 9QD UK</div>
  </section>
</main>
</body>
</html>
```